Magician | Speaker looks for an innovative business card design

I'm a magician and public speaker offering artistic and modern magical experiences.
I'm based in Brussels (Belgium.) I love magic performed up-close, creating a space of intimacy, even when I'm on stage.
The final design should communicate professionalism, elegance, artistry, and a friendly kind personality

I would like to see designs based either on my photos and/or the way I sign my name Remy Vok (see attached files for more info.)
Additional photos and more info about what I offer can be seen at www.remy-vok.net

My current business card design is also attached. I like the fact that the reverse of my current design includes quotes from master magicians about magic, changing the way my participants see the art of magic.

Note: I would like a double-sided card design. However, I need white space on the reverse to be able to write things on for my performances.

Details to include on the card:
Artist name: Remy Vok
Offer: magician + (public) speaker or magic + (public) speaking (the + sign can be replaced by another character, like a bullet or a pipe)
Phone: +32 471 265 903
Email: book@remy-vok.net
(optional) Website: www.remy-vok.net or remy-vok.net

Target Market(s)

Corporate, organisations, companies as well as individuals

Industry/Entity Type

Artists

Colors

Designer to choose colors to be used in the design.

Requirements
Nice to have
• A side with a mirror could be nice

```html
<!DOCTYPE html>
<html lang="en">
<head>
<meta charset="utf-8">
<title>Remy Vok — Business Card</title>
<link href="https://fonts.googleapis.com/css2?family=Saira+Extra+Condensed:wght@300;500;600&display=swap" rel="stylesheet">
<style>
  :root {
    --backdrop: #cdd3d3;
    --paper: #e6e6e4;
    --ink: #1b1b1b;
    --ink-soft: #3a3a3a;
    --night: #121212;
    --night-panel: #0c0c0c;
    --pattern: #1e1e1e;
    --silver: #9c9c9c;
    --silver-dim: #6f6f6f;
    --gilt: #a88e55;
  }
  * { margin: 0; padding: 0; box-sizing: border-box; }
  html, body { width: 1200px; height: 1050px; overflow: hidden; }
  body {
    background: var(--backdrop);
    font-family: "Saira Extra Condensed", "Arial Narrow", sans-serif;
    position: relative;
  }
  .card {
    position: absolute;
    left: 320px;
    width: 560px;
    height: 320px;
    border-radius: 4px;
    box-shadow: 0 12px 30px rgba(0,0,0,0.12);
  }

  /* ---------- Front: light side ---------- */
  .card-front { top: 150px; background: var(--paper); color: var(--ink); }
  .front-frame {
    position: absolute; inset: 28px;
    border: 1.5px solid var(--ink-soft);
    border-radius: 14px;
  }
  .corner-star { position: absolute; width: 14px; height: 14px; }
  .corner-star.tl { left: 8px; top: 8px; }
  .corner-star.tr { right: 8px; top: 8px; }
  .corner-star.bl { left: 8px; bottom: 8px; }
  .corner-star.br { right: 8px; bottom: 8px; }
  .tagline {
    position: absolute;
    font-size: 11px; font-weight: 500; letter-spacing: 1.5px;
    text-transform: uppercase;
  }
  .tagline.top { top: 9px; left: 60px; }
  .tagline.bottom { bottom: 9px; right: 60px; transform: rotate(180deg); }
  .front-name {
    position: absolute; top: 40px; left: 48px;
    font-size: 42px; font-weight: 600; letter-spacing: 2px; line-height: 1;
  }
  .front-roles {
    position: absolute; top: 44px; right: 48px;
    text-align: right; font-size: 16px; font-weight: 600; line-height: 1.25;
    letter-spacing: 1px; text-transform: uppercase;
  }
  .front-contact {
    position: absolute; bottom: 42px; left: 48px;
    font-size: 16px; font-weight: 600; line-height: 1.25;
    letter-spacing: 1px; text-transform: uppercase;
  }
  .front-index {
    position: absolute; bottom: 38px; right: 50px;
    font-size: 40px; font-weight: 600; line-height: 1;
  }

  /* ---------- Back: dark side ---------- */
  .card-back {
    top: 580px; background: var(--night);
    border-bottom: 4px solid var(--gilt);
    overflow: hidden;
  }
  .back-pattern { position: absolute; inset: 0; background: var(--pattern); }
  .back-panel {
    position: absolute; inset: 18px 30px;
    background: radial-gradient(ellipse at center, #1a1a1a 0%, var(--night-panel) 80%);
    display: flex; flex-direction: column; align-items: center; justify-content: center;
    color: var(--silver);
  }
  .back-name {
    font-size: 52px; font-weight: 300; letter-spacing: 5px; line-height: 1;
    text-transform: uppercase;
  }
  .back-rule { width: 90px; height: 1px; background: var(--silver-dim); margin: 18px 0 12px; }
  .back-roles {
    border-left: 1px solid #2c2c2c; border-right: 1px solid #2c2c2c;
    padding: 2px 16px; text-align: center;
    font-size: 13px; font-weight: 500; letter-spacing: 2.5px; line-height: 1.6;
    color: var(--silver-dim); text-transform: uppercase;
  }
  .back-index {
    position: absolute; top: 50%;
    font-size: 30px; font-weight: 300; color: var(--silver-dim);
    margin-top: -18px;
  }
  .back-index.left { left: 18px; transform: rotate(90deg); }
  .back-index.right { right: 18px; transform: rotate(-90deg); }
</style>
</head>
<body>

<section class="card card-front" aria-label="Card front">
  <div class="front-frame"></div>
  <svg class="corner-star tl" viewBox="0 0 20 20"><polygon points="10,1 12.4,7.6 19.5,7.6 13.8,12 16,19 10,14.6 4,19 6.2,12 0.5,7.6 7.6,7.6" fill="none" stroke="#1b1b1b" stroke-width="1.4"/></svg>
  <svg class="corner-star tr" viewBox="0 0 20 20"><polygon points="10,1 12.4,7.6 19.5,7.6 13.8,12 16,19 10,14.6 4,19 6.2,12 0.5,7.6 7.6,7.6" fill="none" stroke="#1b1b1b" stroke-width="1.4"/></svg>
  <svg class="corner-star bl" viewBox="0 0 20 20"><polygon points="10,1 12.4,7.6 19.5,7.6 13.8,12 16,19 10,14.6 4,19 6.2,12 0.5,7.6 7.6,7.6" fill="none" stroke="#1b1b1b" stroke-width="1.4"/></svg>
  <svg class="corner-star br" viewBox="0 0 20 20"><polygon points="10,1 12.4,7.6 19.5,7.6 13.8,12 16,19 10,14.6 4,19 6.2,12 0.5,7.6 7.6,7.6" fill="none" stroke="#1b1b1b" stroke-width="1.4"/></svg>
  <p class="tagline top">Where magic happens</p>
  <p class="tagline bottom">Where magic happens</p>
  <h1 class="front-name">REMY VOK</h1>
  <p class="front-roles">Magician<br>Public speaker</p>
  <p class="front-contact">+32 471 265 903<br>book@remy-vok.net<br>www.remy-vok.net</p>
  <p class="front-index">R</p>
</section>

<section class="card card-back" aria-label="Card back">
  <div class="back-pattern" role="img" aria-label="Fine dark honeycomb texture around the border"></div>
  <div class="back-panel">
    <h2 class="back-name">Remy Vok</h2>
    <div class="back-rule"></div>
    <p class="back-roles">Magician<br>Public speaker</p>
  </div>
  <span class="back-index left">R</span>
  <span class="back-index right">R</span>
</section>

</body>
</html>
```